Business cards for law firm with global theme

I'd like business cards with contact info for two offices. They should include the colors and font of the new logo design, which is a stylized globe with an "F" in it. The feel should be very modern and professional.

```html
<!DOCTYPE html>
<html lang="en">
<head>
<meta charset="UTF-8">
<title>Marvane Law — Business Cards</title>
<link rel="stylesheet" href="https://fonts.googleapis.com/css2?family=Montserrat:wght@400;500;600&display=swap">
<style>
  :root {
    --navy: #1f3c6a;
    --navy-deep: #1a3360;
    --sky: #2aa6e0;
    --white: #ffffff;
    --backdrop: #e9e6e1;
  }
  * { box-sizing: border-box; margin: 0; padding: 0; }
  html, body {
    width: 900px; height: 1200px; overflow: hidden;
    background: var(--backdrop);
    font-family: "Montserrat", Arial, sans-serif;
  }
  .canvas {
    position: relative; width: 900px; height: 1200px;
  }
  .card {
    position: absolute; left: 60px; width: 780px; height: 440px;
    border-radius: 18px; overflow: hidden;
    background: var(--navy);
    box-shadow: 0 6px 18px rgba(0,0,0,0.18);
  }
  .card--contact { top: 120px; }
  .card--brand { top: 640px; background: var(--navy-deep); }

  .card__swoosh { position: absolute; inset: 0; }

  .office {
    position: absolute; left: 48px; color: var(--white);
    font-size: 19px; line-height: 1.42; font-weight: 400;
  }
  .office--main { top: 44px; }
  .office--branch { top: 238px; }
  .office__line { display: block; }
  .office__contact {
    display: flex; align-items: center; gap: 10px;
  }
  .office__icon {
    width: 20px; height: 20px; border-radius: 50%;
    background: var(--white); flex: none;
    display: flex; align-items: center; justify-content: center;
  }
  .office--branch .office__contact { color: var(--sky); }
  .office--branch .office__icon { background: var(--sky); }
  .office__icon svg { width: 12px; height: 12px; }

  .brand {
    position: absolute; inset: 0;
    display: flex; flex-direction: column; align-items: center; justify-content: center;
  }
  .brand__name {
    color: var(--white); font-weight: 500;
    font-size: 62px; letter-spacing: 2px; text-align: center;
    line-height: 1.1; margin-top: 40px;
  }
  .brand__name span { display: block; font-size: 36px; letter-spacing: 6px; }
</style>
</head>
<body>
<main class="canvas">

  <section class="card card--contact" aria-label="Business card, contact side">
    <svg class="card__swoosh" viewBox="0 0 780 440" preserveAspectRatio="none" aria-hidden="true">
      <path d="M240 440 Q560 410 780 190 L780 440 Z" fill="var(--white)"/>
    </svg>

    <div class="office office--main">
      <span class="office__line">118 Larkspur Street NW</span>
      <span class="office__line">Suite 210, Harbor Falls</span>
      <span class="office__line">MI 40217</span>
      <span class="office__contact">
        <span class="office__icon"><svg viewBox="0 0 24 24"><path fill="#1f3c6a" d="M6.6 10.8a15 15 0 006.6 6.6l2.2-2.2a1 1 0 011-.25 11.4 11.4 0 003.6.57 1 1 0 011 1V20a1 1 0 01-1 1A17 17 0 013 4a1 1 0 011-1h3.5a1 1 0 011 1 11.4 11.4 0 00.57 3.6 1 1 0 01-.25 1z"/></svg></span>
        214-555-0186
      </span>
      <span class="office__contact">
        <span class="office__icon"><svg viewBox="0 0 24 24"><path fill="#1f3c6a" d="M6.6 10.8a15 15 0 006.6 6.6l2.2-2.2a1 1 0 011-.25 11.4 11.4 0 003.6.57 1 1 0 011 1V20a1 1 0 01-1 1A17 17 0 013 4a1 1 0 011-1h3.5a1 1 0 011 1 11.4 11.4 0 00.57 3.6 1 1 0 01-.25 1z"/></svg></span>
        214-555-0186
      </span>
      <span class="office__contact">
        <span class="office__icon"><svg viewBox="0 0 24 24"><path fill="#1f3c6a" d="M3 6h18v12H3z M3 6l9 7 9-7" stroke="#fff" stroke-width="1.5"/></svg></span>
        Ellis@mailbox-sample.com
      </span>
    </div>

    <div class="office office--branch">
      <span class="office__line">118 Larkspur Street NW</span>
      <span class="office__line">Suite 210, Harbor Falls</span>
      <span class="office__line">MI 40217</span>
      <span class="office__contact">
        <span class="office__icon"><svg viewBox="0 0 24 24"><path fill="#fff" d="M6.6 10.8a15 15 0 006.6 6.6l2.2-2.2a1 1 0 011-.25 11.4 11.4 0 003.6.57 1 1 0 011 1V20a1 1 0 01-1 1A17 17 0 013 4a1 1 0 011-1h3.5a1 1 0 011 1 11.4 11.4 0 00.57 3.6 1 1 0 01-.25 1z"/></svg></span>
        214-555-0186
      </span>
      <span class="office__contact">
        <span class="office__icon"><svg viewBox="0 0 24 24"><path fill="#fff" d="M6.6 10.8a15 15 0 006.6 6.6l2.2-2.2a1 1 0 011-.25 11.4 11.4 0 003.6.57 1 1 0 011 1V20a1 1 0 01-1 1A17 17 0 013 4a1 1 0 011-1h3.5a1 1 0 011 1 11.4 11.4 0 00.57 3.6 1 1 0 01-.25 1z"/></svg></span>
        214-555-0186
      </span>
      <span class="office__contact">
        <span class="office__icon"><svg viewBox="0 0 24 24"><path fill="#fff" d="M3 6h18v12H3z M3 6l9 7 9-7" stroke="#2aa6e0" stroke-width="1.5"/></svg></span>
        Ellis@mailbox-sample.com
      </span>
    </div>
  </section>

  <section class="card card--brand" aria-label="Business card, brand side">
    <div class="brand">
      <p class="brand__name">MARVANE<span>LAW</span></p>
    </div>
  </section>

</main>
</body>
</html>
```